Brisk Rig Vitals: Truck Smoke Check Company

I need a logo for a truck health company in California called "Brisk Rig Vitals". This company does smoke checks for heavy duty diesel trucks under the Pacific Clean Skies Council (PCSC) called HD I/M tests. I want the brand to feel reliable.

Target Market(s)

California Diesel Trucks. Individual truck drivers and trucking companies.

Industry/Entity Type

Automotive

Contact Information for Business Card

Company Name, Slogan, contact information. marcotellez@briskrigvitals-example.com

```html
<!DOCTYPE html>
<html lang="en">
<head>
<meta charset="utf-8">
<title>Brisk Rig Vitals – Business Card</title>
<link rel="stylesheet" href="https://fonts.googleapis.com/css2?family=Anton&family=Montserrat:wght@400;500;800&family=Oswald:wght@600&display=swap">
<style>
  :root {
    --page-bg: #ece8e1;
    --card-dark: #1e1e1e;
    --ink-dark: #0c0c0c;
    --ink-dark-soft: #111111;
    --card-light: #ffffff;
    --navy: #27307a;
    --navy-band: #3b4a80;
    --navy-soft: #6d7bab;
    --orange: #f2a20c;
    --ink: #111111;
  }
  * { margin: 0; padding: 0; box-sizing: border-box; }
  html, body { width: 1200px; height: 675px; overflow: hidden; background: var(--page-bg); }
  .canvas { position: relative; width: 1200px; height: 675px; }

  .card {
    position: absolute; top: 182px; width: 540px; height: 310px;
    border-radius: 22px; overflow: hidden;
    box-shadow: 0 6px 18px rgba(0,0,0,0.18);
  }

  /* Front (dark) */
  .card-front { left: 45px; background: var(--card-dark); }
  .front-mark {
    position: absolute; left: 0; right: 0; top: 62px;
    display: flex; align-items: center; justify-content: center; gap: 10px;
  }
  .mark-dot { width: 22px; height: 22px; border-radius: 50%; background: var(--ink-dark); }
  .front-mark .mark-name {
    font-family: "Anton", sans-serif; font-size: 30px; letter-spacing: 1px;
    color: var(--ink-dark); text-transform: uppercase;
  }
  .front-wordmark {
    position: absolute; left: 0; right: 0; top: 128px; text-align: center;
    font-family: "Anton", sans-serif; font-size: 56px; line-height: 1; color: var(--ink-dark);
  }
  .front-slogan {
    position: absolute; left: 0; right: 0; top: 204px; text-align: center;
    font-family: "Montserrat", sans-serif; font-size: 15px; letter-spacing: 1px; color: var(--ink-dark-soft);
  }

  /* Back (white) */
  .card-back { left: 615px; background: var(--card-light); }
  .swoosh { position: absolute; inset: 0; width: 540px; height: 310px; }

  .brand-block { position: absolute; left: 28px; top: 112px; width: 222px; }
  .brand-mark { display: flex; align-items: center; gap: 7px; margin-bottom: 8px; }
  .brand-mark .mark-dot { width: 16px; height: 16px; background: var(--navy); }
  .brand-mark .mark-name {
    font-family: "Anton", sans-serif; font-size: 17px; letter-spacing: 1px;
    color: var(--navy); text-transform: uppercase;
  }
  .brand-wordmark { font-family: "Anton", sans-serif; font-size: 29px; line-height: 1.05; color: var(--navy); }
  .brand-slogan { font-family: "Montserrat", sans-serif; font-size: 9px; font-weight: 500; color: var(--navy); margin-top: 3px; white-space: nowrap; }
  .brand-web { font-family: "Oswald", sans-serif; font-weight: 600; font-size: 13.5px; color: var(--orange); margin-top: 6px; }

  .divider { position: absolute; left: 258px; top: 62px; width: 2px; height: 150px; background: var(--navy); }

  .person { position: absolute; left: 276px; top: 60px; }
  .person-name { font-family: "Montserrat", sans-serif; font-weight: 800; font-size: 28px; color: var(--navy); line-height: 1; }
  .person-title { font-family: "Montserrat", sans-serif; font-size: 17px; color: var(--ink); margin-top: 4px; }

  .contacts { position: absolute; left: 276px; top: 140px; list-style: none; }
  .contacts li {
    display: flex; align-items: center; gap: 7px; margin-bottom: 6px;
    font-family: "Montserrat", sans-serif; font-weight: 500; font-size: 10.5px; color: var(--ink);
    white-space: nowrap;
  }
  .contacts svg { width: 15px; height: 15px; flex: none; }
</style>
</head>
<body>
<main class="canvas">

  <section class="card card-front" aria-label="Card front">
    <div class="front-mark">
      <span class="mark-dot"></span>
      <span class="mark-name">Brisk Rig Vitals</span>
    </div>
    <h1 class="front-wordmark">Brisk Rig Vitals</h1>
    <p class="front-slogan">Trusted Diesel Testing, Cleaner Roads Ahead.</p>
  </section>

  <section class="card card-back" aria-label="Card back">
    <svg class="swoosh" viewBox="0 0 540 310" preserveAspectRatio="none" aria-hidden="true">
      <path d="M0,292 C210,282 400,225 540,118" fill="none" stroke="var(--navy-soft)" stroke-width="3"/>
      <path d="M0,306 C230,300 420,250 540,140 L540,310 L0,310 Z" fill="var(--navy-band)"/>
    </svg>

    <div class="brand-block">
      <div class="brand-mark">
        <span class="mark-dot"></span>
        <span class="mark-name">Brisk Rig Vitals</span>
      </div>
      <div class="brand-wordmark">Brisk Rig Vitals</div>
      <div class="brand-slogan">Trusted Diesel Testing, Cleaner Roads Ahead.</div>
      <div class="brand-web">www.briskrigvitals-example.com</div>
    </div>

    <div class="divider"></div>

    <div class="person">
      <div class="person-name">MY NAME</div>
      <div class="person-title">President</div>
    </div>

    <ul class="contacts">
      <li>
        <svg viewBox="0 0 16 16" aria-hidden="true"><circle cx="8" cy="8" r="7" fill="none" stroke="#111" stroke-width="1.2"/><path d="M5.5 4.5l1.4 1.6-.8 1c.6 1.2 1.4 2 2.6 2.6l1-.8 1.6 1.4-.9 1.2c-2.8-.4-5-2.6-5.4-5.4z" fill="#111"/></svg>
        555 010 2846
      </li>
      <li>
        <svg viewBox="0 0 16 16" aria-hidden="true"><circle cx="8" cy="8" r="7" fill="none" stroke="#111" stroke-width="1.2"/><rect x="5.6" y="3.8" width="4.8" height="8.4" rx="0.8" fill="none" stroke="#111" stroke-width="1.1"/></svg>
        555 010 7193
      </li>
      <li>
        <svg viewBox="0 0 16 16" aria-hidden="true"><circle cx="8" cy="8" r="7" fill="#111"/><rect x="4.3" y="5.4" width="7.4" height="5.2" fill="#fff"/><path d="M4.3 5.4L8 8.4l3.7-3" fill="none" stroke="#111" stroke-width="0.9"/></svg>
        marcotellez@briskrigvitals-example.com
      </li>
    </ul>
  </section>

</main>
</body>
</html>
```